Doctor in Veterinary Medecine/ veterinarian

I am a vet and would like a buisness card which is simple yet elegant and professional.
My aim is to help as much animals as I can. My main field of expertise are dogs and cats. I would like the card to reflect a "family doctor" feeling.
It should not be the traditional picture of a paw or a dog but yet it should have a sign of a pet on it. I would like to have my name Lina Haddour as well as my profession D.V.M and my number.

Target Market(s)

Lebanese population who have pets

Industry/Entity Type

Doctor

Contact Information for Business Card

Should contain my profession " D.V.M", my full name "Lina Haddour" and my number "0096171552934"

Requirements
Must have
• A certain picture depicting my profession
Nice to have
• Some sort of picture related to pets and animals
Should not have
• A picture of a paw or a dog. I need something more creative

```html
<!DOCTYPE html>
<html lang="en">
<head>
<meta charset="utf-8">
<title>Lina Haddour, DVM – Business Card</title>
<link rel="stylesheet" href="https://fonts.googleapis.com/css2?family=Montserrat:wght@300;400;700&display=swap">
<style>
  :root {
    --stage: #e9ebee;
    --blue-light: #5fc0e2;
    --blue-deep: #1a88c6;
    --white: #ffffff;
    --paper: #f4f5f6;
    --line: rgba(255,255,255,0.55);
  }
  * { margin: 0; padding: 0; box-sizing: border-box; }
  html, body {
    width: 1200px; height: 750px; overflow: hidden;
    background: var(--stage);
    font-family: "Montserrat", Arial, sans-serif;
  }
  .card {
    position: absolute; left: 100px; top: 85px;
    width: 1000px; height: 580px;
    border-radius: 36px; overflow: hidden;
    background: linear-gradient(160deg, var(--blue-light) 0%, var(--blue-deep) 75%);
    box-shadow: 0 10px 30px rgba(0,0,0,0.18);
  }
  .card__base-band {
    position: absolute; left: 250px; right: 0; bottom: 0; height: 112px;
    background: var(--paper);
    border-top-left-radius: 40px;
  }
  .card__side-tab {
    position: absolute; left: 0; top: 190px; width: 42px; height: 290px;
    background: var(--paper);
    border-top-right-radius: 14px; border-bottom-right-radius: 14px;
  }
  .contact-icon {
    position: absolute; left: 28px; width: 54px; height: 54px;
    border-radius: 50%;
    background: var(--blue-deep);
    border: 4px solid var(--paper);
    display: flex; align-items: center; justify-content: center;
  }
  .contact-icon svg { width: 26px; height: 26px; }
  .contact-icon--person { top: 218px; }
  .contact-icon--phone { top: 302px; }
  .contact-icon--mail { top: 386px; }

  .identity { position: absolute; left: 118px; top: 178px; color: var(--white); }
  .identity__name {
    font-weight: 700; font-size: 30px; letter-spacing: 0.5px; text-transform: uppercase;
  }
  .identity__title {
    font-weight: 300; font-size: 22px; letter-spacing: 2px; margin-top: 2px;
  }
  .identity__rule {
    position: absolute; left: 340px; top: 12px; width: 180px; height: 1px; background: var(--line);
  }
  .contact-line {
    position: absolute; left: 118px; color: var(--white);
    font-weight: 400; font-size: 27px; letter-spacing: 0.5px;
  }
  .contact-line--phone { top: 313px; }
  .contact-line--mail { top: 397px; }

  .pet-artwork {
    position: absolute; left: 560px; top: 100px; width: 380px; height: 370px;
    background: radial-gradient(ellipse at 55% 60%, rgba(255,255,255,0.9) 0%, rgba(255,255,255,0.55) 45%, rgba(255,255,255,0) 72%);
  }
</style>
</head>
<body>
  <div class="card">
    <div class="card__base-band"></div>
    <div class="card__side-tab"></div>

    <div class="pet-artwork" role="img" aria-label="White silhouettes of a dog, a cat and a rabbit standing together"></div>

    <div class="contact-icon contact-icon--person">
      <svg viewBox="0 0 24 24" fill="#ffffff"><circle cx="12" cy="8" r="4.5"/><path d="M3.5 21c0-4.7 3.8-7.5 8.5-7.5s8.5 2.8 8.5 7.5z"/></svg>
    </div>
    <div class="contact-icon contact-icon--phone">
      <svg viewBox="0 0 24 24" fill="none" stroke="#ffffff" stroke-width="2"><rect x="6.5" y="2.5" width="11" height="19" rx="2"/><line x1="10.5" y1="18.5" x2="13.5" y2="18.5"/></svg>
    </div>
    <div class="contact-icon contact-icon--mail">
      <svg viewBox="0 0 24 24" fill="none" stroke="#ffffff" stroke-width="2"><rect x="2.5" y="5.5" width="19" height="13" rx="1.5"/><path d="M3 6.5l9 7 9-7"/></svg>
    </div>

    <div class="identity">
      <div class="identity__name">Lina Haddour</div>
      <div class="identity__title">DVM</div>
      <div class="identity__rule"></div>
    </div>
    <div class="contact-line contact-line--phone">0096171552934</div>
    <div class="contact-line contact-line--mail">linahaddour@petmail.com</div>
  </div>
</body>
</html>
```